Business card for boutique investment firm

Need a business card designed for our boutique investment firm called "BrightLedger Investment Fee Advisors". We help investors achieve lower fees through negotiation on their behalf. We have a logo to work with and a color palette. The card should incorporate our tag line "The power of small changes" and space for relevant details. The look and feel should reflect the logo and our brand personality: Humble, Trustworthy, Friendly

Target Market(s)

High net worth investors who are looking for clarity around how they are being charged by their investment advisor

Industry/Entity Type

Boutique

Requirements
Must have
• Logo
Tag line: The Power of Small Changes
Space for relevant contact details: name, title, phone, email, URL, mailing address

Use these fonts: 'AvantGarde Bk BT' and 'AvantGarde Bk BT Demi'
Use these colors:
Orange = C-0 / M-60 / Y-100 / K-0
Grey = C-0 / M-0 / Y-0 / K-60

```html
<!DOCTYPE html>
<html lang="en">
<head>
<meta charset="utf-8">
<title>BrightLedger Investment Fee Advisors — Business Card</title>
<link rel="stylesheet" href="https://fonts.googleapis.com/css2?family=Questrial&family=Poppins:wght@600&display=swap">
<style>
  :root {
    --brand-orange: #ff6600;
    --brand-grey: #6d6e71;
    --card-white: #ffffff;
    --page-bg: #f4f4f4;
    --card-edge: #e2e2e2;
    --font-book: 'Questrial', sans-serif;
    --font-demi: 'Poppins', sans-serif;
  }
  html, body {
    margin: 0;
    padding: 0;
    width: 1200px;
    height: 1000px;
    overflow: hidden;
    background: var(--page-bg);
  }
  .canvas {
    position: relative;
    width: 1200px;
    height: 1000px;
  }
  .card {
    position: absolute;
    background: var(--card-white);
    border: 1px solid var(--card-edge);
    box-sizing: border-box;
    overflow: hidden;
  }

  /* Front */
  .card-front {
    left: 30px;
    top: 50px;
    width: 740px;
    height: 410px;
  }
  .front-band {
    position: absolute;
    left: 0;
    top: 0;
    width: 100%;
    height: 352px;
    background: var(--brand-orange);
  }
  .brand-lockup {
    position: absolute;
    left: 78px;
    top: 92px;
    display: flex;
    align-items: center;
    gap: 26px;
  }
  .brand-mark {
    width: 118px;
    height: 118px;
    flex: none;
  }
  .brand-name {
    font-family: var(--font-book);
    font-weight: 400;
    color: var(--card-white);
    margin: 0;
    line-height: 1;
  }
  .brand-name .name-main {
    display: block;
    font-size: 84px;
    letter-spacing: -2px;
  }
  .brand-name .name-sub {
    display: block;
    font-size: 25px;
    letter-spacing: 4px;
    margin-top: 8px;
  }
  .tagline {
    position: absolute;
    right: 22px;
    bottom: 18px;
    margin: 0;
    font-family: var(--font-book);
    font-size: 23px;
    letter-spacing: 0.5px;
    text-transform: uppercase;
    color: var(--brand-grey);
  }

  /* Back */
  .card-back {
    left: 430px;
    top: 530px;
    width: 720px;
    height: 410px;
  }
  .back-mark {
    position: absolute;
    left: 58px;
    top: 38px;
    width: 150px;
    height: 150px;
  }
  .contact {
    position: absolute;
    right: 50px;
    top: 82px;
    text-align: right;
    font-style: normal;
    font-family: var(--font-book);
    font-size: 30px;
    line-height: 38px;
    color: var(--brand-grey);
  }
  .contact p { margin: 0; }
  .contact .accent {
    font-family: var(--font-demi);
    font-weight: 600;
    color: var(--brand-orange);
  }
  .contact .person-title { margin-bottom: 26px; }
</style>
</head>
<body>
<main class="canvas">

  <section class="card card-front" aria-label="Business card front">
    <div class="front-band">
      <div class="brand-lockup">
        <svg class="brand-mark" viewBox="0 0 120 120" aria-hidden="true">
          <circle cx="60" cy="60" r="60" fill="var(--card-white)"/>
        </svg>
        <h1 class="brand-name">
          <span class="name-main">BrightLedger</span>
          <span class="name-sub">Investment Fee Advisors</span>
        </h1>
      </div>
    </div>
    <p class="tagline">The Power of Small Changes</p>
  </section>

  <section class="card card-back" aria-label="Business card back">
    <svg class="back-mark" viewBox="0 0 150 150" aria-hidden="true">
      <circle cx="75" cy="75" r="75" fill="var(--brand-orange)"/>
    </svg>
    <address class="contact">
      <p class="accent person-name">Name</p>
      <p class="person-title">Title</p>
      <p class="accent phone">000.000.0000</p>
      <p class="mailing">mailing address</p>
      <p class="email">email</p>
      <p class="url">URL</p>
    </address>
  </section>

</main>
</body>
</html>
```